Eye catching while remaining subtle, stylish and professional

Plover Works are a Heatpump and Air Conditioning Company. I would like stationary that would be suitable to use for letters, quoting invoicing. The final design should communicate a trade/service type industry that is clean and professional

I would like the designer to also offer a Business card option as well.

Details should include company logo as attached. Company details. Name, Address, Phone, Email and Website. You can use generic details until a final design is chosen

Target Market(s)

Trade/Service Industry

Industry/Entity Type

Air Conditioning

Requirements
Must have
• LOGO, Company contact details
Nice to have
• Watermark

```html
<!DOCTYPE html>
<html lang="en">
<head>
<meta charset="utf-8">
<title>Plover Works – Stationery Set</title>
<link rel="stylesheet" href="https://fonts.googleapis.com/css2?family=Exo+2:wght@400;600&family=Arimo:wght@400;700&display=swap">
<style>
  :root {
    --bg: #e9eaec;
    --paper: #ffffff;
    --brand-blue: #3db3e6;
    --blue-light: #8ad6f3;
    --blue-deep: #2fa6dc;
    --grey-swoosh: #c4c5c7;
    --grey-text: #555a60;
    --ink: #333333;
    --watermark: rgba(61, 179, 230, 0.12);
  }
  * { box-sizing: border-box; margin: 0; padding: 0; }
  html, body { width: 1200px; height: 937px; overflow: hidden; }
  body { background: var(--bg); position: relative; font-family: "Arimo", Arial, sans-serif; color: var(--ink); }

  .piece { position: absolute; background: var(--paper); overflow: hidden; box-shadow: 0 2px 6px rgba(0,0,0,0.12); }
  .wave { position: absolute; left: 0; bottom: 0; width: 100%; display: block; }

  .wordmark { font-family: "Exo 2", Arial, sans-serif; font-weight: 600; color: var(--brand-blue); white-space: nowrap; display: flex; align-items: center; }
  .wordmark .dot { display: inline-block; border-radius: 50%; background: var(--brand-blue); }

  .watermark-ring { position: absolute; border-radius: 50%; border-style: solid; border-color: var(--watermark); }

  .site { position: absolute; font-family: "Exo 2", Arial, sans-serif; color: #fff; letter-spacing: 0.12em; white-space: nowrap; }

  /* Letterhead */
  .letterhead { left: 185px; top: 66px; width: 386px; height: 546px; }
  .letterhead .wordmark { position: absolute; left: 50px; top: 50px; font-size: 20px; }
  .letterhead .wordmark .dot { width: 8px; height: 8px; margin-right: 6px; }
  .letterhead .watermark-ring { left: 95px; top: 150px; width: 130px; height: 130px; border-width: 22px; }
  .letter-body { position: absolute; left: 36px; top: 138px; width: 295px; font-size: 5.3px; line-height: 7px; color: var(--grey-text); }
  .letter-body p { margin-bottom: 8px; }
  .letter-body .gap { margin-bottom: 22px; }
  .letter-body strong { color: var(--ink); }
  .signature { width: 24px; height: 14px; background: #d6d6d6; margin: 4px 0 6px; }
  .contact-list { position: absolute; left: 224px; top: 488px; list-style: none; font-size: 4.6px; line-height: 8px; color: #fff; }
  .contact-list li { display: flex; align-items: center; }
  .contact-list .icon { width: 5px; height: 5px; border-radius: 50%; background: #fff; margin-right: 4px; }

  /* Folder */
  .folder { left: 636px; top: 40px; width: 458px; height: 576px; }
  .folder .watermark-ring { left: 120px; top: 140px; width: 220px; height: 220px; border-width: 30px; border-color: rgba(61,179,230,0.06); }
  .folder .wordmark { position: absolute; left: 0; right: 0; top: 205px; justify-content: center; font-size: 54px; }
  .folder .wordmark .dot { width: 18px; height: 18px; margin-right: 12px; }
  .folder .site { right: 16px; bottom: 12px; font-size: 11px; }

  /* Business cards */
  .card { left: 46px; width: 175px; height: 100px; }
  .card-front { top: 658px; }
  .card-back { top: 785px; }
  .card .wordmark { position: absolute; left: 16px; font-size: 11px; }
  .card .wordmark .dot { width: 5px; height: 5px; margin-right: 4px; }
  .card-front .wordmark { top: 22px; }
  .card-back .wordmark { top: 36px; }
  .card-person { position: absolute; left: 6px; top: 55px; font-size: 6px; line-height: 7px; color: #2b3a8c; }
  .card-person .title { font-size: 4px; color: var(--ink); }
  .card .contact-list { left: 96px; top: 56px; font-size: 3.4px; line-height: 5.5px; }
  .card .contact-list .icon { width: 3.5px; height: 3.5px; margin-right: 3px; }

  /* Envelopes */
  .envelope-front { left: 265px; top: 672px; width: 431px; height: 207px; }
  .envelope-front .wordmark { position: absolute; left: 34px; top: 55px; font-size: 22px; }
  .envelope-front .wordmark .dot { width: 8px; height: 8px; margin-right: 6px; }
  .envelope-front .watermark-ring { left: 20px; top: 95px; width: 120px; height: 120px; border-width: 24px; }
  .envelope-front .site { right: 104px; bottom: 12px; font-size: 9px; }

  .envelope-back { left: 736px; top: 671px; width: 432px; height: 208px; }
  .flap { position: absolute; left: 0; top: 0; width: 100%; height: 71px; border-radius: 0 0 30px 30px; background: linear-gradient(180deg, var(--blue-light), var(--brand-blue)); box-shadow: 0 2px 4px rgba(0,0,0,0.15); }
  .envelope-back .site { left: 0; right: 0; top: 28px; text-align: center; font-size: 11.5px; }
  .envelope-back .watermark-ring { right: -30px; top: 80px; width: 120px; height: 120px; border-width: 24px; }
</style>
</head>
<body>

<svg width="0" height="0" style="position:absolute" aria-hidden="true">
  <defs>
    <linearGradient id="wave-blue" x1="0" y1="0" x2="1" y2="1">
      <stop offset="0" stop-color="#a4e0f6"/>
      <stop offset="1" stop-color="#35ade2"/>
    </linearGradient>
  </defs>
</svg>

<!-- Letterhead -->
<section class="piece letterhead">
  <div class="watermark-ring"></div>
  <div class="wordmark"><span class="dot"></span>Plover Works</div>
  <div class="letter-body">
    <p>July 2, 2012</p>
    <p><strong>Dear Sir,</strong><br>12 Kestrel Lane, Country Name</p>
    <p class="gap">Thank you for choosing us for your heating and cooling needs. This letter confirms the details of your recent service visit, including the heat pump inspection, filter replacement and refrigerant check. Our technician found the system running well and has noted a few small items for your next scheduled maintenance appointment later this year.</p>
    <p class="gap">A full quotation for the recommended work is attached. Please review it at your convenience and contact our office with any questions.</p>
    <p>We are happy to book the installation at a time that suits you. Our team will protect your home, remove all packaging and explain how to use the new controls before leaving. Every installation is covered by our workmanship guarantee, and we will call you after one month to make sure everything is working as it should.</p>
    <p>Best Regards,</p>
    <div class="signature" role="img" aria-label="Handwritten signature"></div>
    <p><strong>Rowan Hale</strong><br>Director<br><br>12 Kestrel Lane, Country Name</p>
  </div>
  <svg class="wave" viewBox="0 0 400 220" preserveAspectRatio="none" style="height:215px" aria-hidden="true">
    <path d="M0,190 C130,178 290,115 400,45 L400,220 L0,220Z" fill="url(#wave-blue)"/>
    <path d="M0,176 C130,162 290,100 400,28 L400,48 C290,118 130,182 0,192Z" fill="#fff"/>
    <path d="M0,158 C130,146 290,75 400,0 L400,20 C290,95 130,166 0,178Z" fill="var(--grey-swoosh)"/>
    <path d="M230,140 C300,112 360,72 400,40 L400,48 C360,80 300,118 230,140Z" fill="var(--brand-blue)"/>
  </svg>
  <ul class="contact-list">
    <li><span class="icon"></span>012 345 6789</li>
    <li><span class="icon"></span>012 345 6780</li>
    <li><span class="icon"></span>info@ploverworks.com</li>
    <li><span class="icon"></span>www.ploverworks.com</li>
    <li><span class="icon"></span>12 Kestrel Lane, Country Name</li>
  </ul>
</section>

<!-- Presentation folder -->
<section class="piece folder">
  <div class="watermark-ring"></div>
  <div class="wordmark"><span class="dot"></span>Plover Works</div>
  <svg class="wave" viewBox="0 0 400 220" preserveAspectRatio="none" style="height:260px" aria-hidden="true">
    <path d="M0,195 C130,180 290,115 400,45 L400,220 L0,220Z" fill="url(#wave-blue)"/>
    <path d="M0,180 C130,165 290,100 400,28 L400,48 C290,118 130,186 0,196Z" fill="#fff"/>
    <path d="M0,162 C130,148 290,75 400,0 L400,22 C290,96 130,170 0,182Z" fill="var(--grey-swoosh)"/>
    <path d="M200,148 C290,118 355,78 400,44 L400,54 C355,88 290,125 200,148Z" fill="var(--brand-blue)"/>
  </svg>
  <div class="site">www.ploverworks.com</div>
</section>

<!-- Business card front -->
<section class="piece card card-front">
  <div class="wordmark"><span class="dot"></span>Plover Works</div>
  <div class="card-person">DANA WHITFIELD<br><span class="title">Managing Director</span></div>
  <svg class="wave" viewBox="0 0 400 220" preserveAspectRatio="none" style="height:90px" aria-hidden="true">
    <path d="M0,190 C130,178 290,115 400,45 L400,220 L0,220Z" fill="url(#wave-blue)"/>
    <path d="M0,176 C130,162 290,100 400,28 L400,48 C290,118 130,182 0,192Z" fill="#fff"/>
    <path d="M0,158 C130,146 290,75 400,0 L400,20 C290,95 130,166 0,178Z" fill="var(--grey-swoosh)"/>
  </svg>
  <ul class="contact-list">
    <li><span class="icon"></span>012 345 6789</li>
    <li><span class="icon"></span>012 345 6780</li>
    <li><span class="icon"></span>info@ploverworks.com</li>
    <li><span class="icon"></span>www.ploverworks.com</li>
    <li><span class="icon"></span>12 Kestrel Lane, Country Name</li>
  </ul>
</section>

<!-- Business card back -->
<section class="piece card card-back">
  <div class="wordmark"><span class="dot"></span>Plover Works</div>
  <svg class="wave" viewBox="0 0 400 220" preserveAspectRatio="none" style="height:90px" aria-hidden="true">
    <path d="M0,190 C130,178 290,115 400,45 L400,220 L0,220Z" fill="url(#wave-blue)"/>
    <path d="M0,176 C130,162 290,100 400,28 L400,48 C290,118 130,182 0,192Z" fill="#fff"/>
    <path d="M0,158 C130,146 290,75 400,0 L400,20 C290,95 130,166 0,178Z" fill="var(--grey-swoosh)"/>
  </svg>
</section>

<!-- Envelope front -->
<section class="piece envelope-front">
  <div class="watermark-ring"></div>
  <div class="wordmark"><span class="dot"></span>Plover Works</div>
  <svg class="wave" viewBox="0 0 400 220" preserveAspectRatio="none" style="height:207px" aria-hidden="true">
    <path d="M0,195 C130,180 290,120 400,60 L400,220 L0,220Z" fill="url(#wave-blue)"/>
    <path d="M0,182 C130,166 290,105 400,40 L400,62 C290,125 130,188 0,198Z" fill="#fff"/>
    <path d="M0,164 C130,150 290,80 400,10 L400,32 C290,100 130,172 0,184Z" fill="var(--grey-swoosh)"/>
    <path d="M220,138 C300,110 360,80 400,58 L400,66 C360,88 300,118 220,138Z" fill="var(--brand-blue)"/>
  </svg>
  <div class="site">www.ploverworks.com</div>
</section>

<!-- Envelope back -->
<section class="piece envelope-back">
  <div class="watermark-ring"></div>
  <div class="flap"></div>
  <div class="site">www.ploverworks.com</div>
</section>

</body>
</html>
```